Lark and Fern: Prespective and Balence in People's Lives Needs a Buissness Card Design

Lark and Fern Community Center is an organization that seeks to bring balance into people's lives. Main services include: guided meditation, group brainstorming, and guided counseling. Lark and Fern combines Eastern practices, i.e. Buddhism, Hinduism, and Taoism, with Western practices: therapy, group brainstorming and healing. We would like a double sided card: 1) front vertical with image, 2) back horizontal with information. The main colors for the card are red, white, black. Different finishes would be nice--please no high gloss. Matte, pearlized, embossing--used tactfully and sparingly would be nice. The card should convey balance/harmony in a modern world.

```html
<!DOCTYPE html>
<html lang="en">
<head>
<meta charset="UTF-8">
<title>Lark and Fern Community Center – Business Card</title>
<link rel="stylesheet" href="https://fonts.googleapis.com/css2?family=Alegreya:ital,wght@0,400;0,700;1,400;1,700&display=swap">
<style>
  :root {
    --ink: #0b0b0b;
    --paper: #fbfbf9;
    --red: #e3161f;
    --backdrop: #e7e4e2;
    --serif: "Alegreya", Georgia, serif;
  }
  * { box-sizing: border-box; margin: 0; padding: 0; }
  html, body { width: 1200px; height: 1000px; overflow: hidden; }
  body { background: var(--backdrop); font-family: var(--serif); position: relative; }

  .card {
    position: absolute;
    border-radius: 22px;
    overflow: hidden;
    background: var(--paper);
    box-shadow: 0 10px 28px rgba(0,0,0,.22);
  }

  /* Front – vertical */
  .card--front { left: 80px; top: 185px; width: 360px; height: 630px; }
  .front__dark-half {
    position: absolute; top: 0; right: 0; width: 50%; height: 100%;
    background: var(--ink);
  }
  .front__mark {
    position: absolute; left: 50%; top: 40%;
    transform: translate(-50%, -50%);
    display: flex; flex-direction: column; align-items: center; gap: 22px;
  }
  .front__dot {
    width: 190px; height: 190px; border-radius: 50%;
    background: var(--red);
  }
  .front__name {
    font-weight: 700; font-size: 30px; color: var(--red);
    white-space: nowrap;
  }

  /* Back – horizontal */
  .card--back { left: 520px; top: 340px; width: 580px; height: 330px; }
  .back__band {
    position: absolute; left: 0; top: 0; width: 100%; height: 42%;
    background: var(--ink);
  }
  .back__title {
    position: absolute; top: 22px; left: 60px; right: 24px;
    color: var(--paper); text-align: center;
  }
  .back__org { font-size: 27px; font-weight: 700; font-style: italic; letter-spacing: .5px; }
  .back__tagline { font-size: 15px; font-style: italic; font-weight: 700; margin-top: 2px; letter-spacing: .3px; }

  .back__role {
    position: absolute; left: 30px; top: 112px;
    font-size: 17px; font-style: italic; color: var(--paper);
  }
  .back__contact {
    position: absolute; left: 30px; top: 146px;
    font-style: italic; font-weight: 700; color: var(--ink);
  }
  .back__person { font-size: 20px; color: var(--red); margin-bottom: 8px; }
  .back__line { font-size: 14.5px; line-height: 1.5; }

  .back__mark {
    position: absolute; left: 66%; top: 42%;
    transform: translate(-50%, -44px);
    display: flex; flex-direction: column; align-items: center; gap: 8px;
  }
  .back__dot { width: 88px; height: 88px; border-radius: 50%; background: var(--red); }
  .back__name { font-size: 16px; font-weight: 700; color: var(--red); white-space: nowrap; }
</style>
</head>
<body>

  <section class="card card--front" aria-label="Card front">
    <div class="front__dark-half"></div>
    <div class="front__mark">
      <div class="front__dot"></div>
      <div class="front__name">Lark and Fern</div>
    </div>
  </section>

  <section class="card card--back" aria-label="Card back">
    <div class="back__band"></div>
    <header class="back__title">
      <h1 class="back__org">Lark and Fern Community center</h1>
      <p class="back__tagline">Clarity and Calm for Everyday Living</p>
    </header>

    <p class="back__role">Director</p>

    <div class="back__contact">
      <p class="back__person">Mara Quill</p>
      <p class="back__line">Fern Lane 12, 2040 Dalby</p>
      <p class="back__line">090-5550-218</p>
      <p class="back__line">hello@larkfern.org</p>
      <p class="back__line">larkfern.org</p>
    </div>

    <div class="back__mark">
      <div class="back__dot"></div>
      <div class="back__name">Lark and Fern</div>
    </div>
  </section>

</body>
</html>
```